Service Plans and Offerings - One Page

We are looking for an 8.5 x 11 one page in a portrait orientation that advertises our product and service offerings on one side and our logo and a slogan, "Reliable Managed IT Services & Support" - "TALMERO is ready to earn your trust" on the other with TALMERO contact information.

This brochure would be left at prospect client's business, so it needs to be inviting, professional, and clear.

Attached is one excel sheet with 4 columns representing our Service Plans and Offerings (Ideas on the descriptive names for the different service offering level is welcome) that we would like you to use for inspiration for the written content in the handout.

The brochure should have the TALMERO contact information on the bottom of the services description page and on the other side of the page (not necessary located at bottom). TALMERO contact information (email, phone, website) will provided to contest winner.

Please be creative with both the content and the design.

Target Market(s)

Small to medium companies with 5-50 seats.

Industry/Entity Type

Information Technology (IT) Managed Service Provider

Font styles to use
Serif

Colors
0094D4
00A9DD
6FCCEA
C7EBF8
E9F6FB

Requirements
Must have
• Clear and professional representation of TALMERO Product Services Plans and easy to read TALMERO contact information.

```html
<!DOCTYPE html>
<html lang="en">
<head>
<meta charset="utf-8">
<title>TALMERO – Reliable Managed IT Services &amp; Support</title>
<link rel="stylesheet" href="https://fonts.googleapis.com/css2?family=Open+Sans:wght@400;600;700&family=Ubuntu:wght@700&display=swap">
<style>
  :root {
    --navy: #111a4f;
    --navy-deep: #0a0f3a;
    --navy-table: #13215a;
    --brand-blue: #0094d4;
    --sky: #00a9dd;
    --ice: #6fccea;
    --band-blue: #2b7fd4;
    --white: #ffffff;
    --rule: rgba(255, 255, 255, 0.35);
    --backdrop: #eef0f3;
  }
  * { margin: 0; padding: 0; box-sizing: border-box; }
  html, body { width: 901px; height: 1200px; overflow: hidden; background: var(--backdrop); }
  body { position: relative; font-family: "Open Sans", Arial, sans-serif; }

  .sheet {
    position: absolute;
    top: 328px;
    width: 420px;
    height: 543px;
    box-shadow: 0 4px 10px rgba(0, 0, 0, 0.18);
    overflow: hidden;
  }
  .sheet--front { left: 20px; }
  .sheet--back { left: 461px; }
  .page {
    position: relative;
    width: 515px;
    height: 665px;
    transform: scale(0.8155);
    transform-origin: 0 0;
    overflow: hidden;
  }

  /* ---------- front side ---------- */
  .front { background: var(--white); }
  .front__art { position: absolute; inset: 0; }
  .brand {
    position: absolute;
    display: flex;
    align-items: center;
    gap: 8px;
  }
  .brand__dot { border-radius: 50%; background: var(--brand-blue); flex: none; }
  .brand__name { font-weight: 700; letter-spacing: 1.5px; }
  .front .brand { left: 31px; top: 33px; }
  .front .brand__dot { width: 28px; height: 28px; }
  .front .brand__name { font-size: 28px; color: var(--brand-blue); }

  .headline {
    position: absolute;
    right: 31px;
    top: 24px;
    text-align: right;
    font-family: "Ubuntu", "Trebuchet MS", sans-serif;
    font-weight: 700;
    font-size: 45px;
    line-height: 52px;
    color: var(--white);
  }
  .slogan {
    position: absolute;
    right: 31px;
    top: 252px;
    text-align: right;
    font-size: 25px;
    line-height: 35px;
    color: var(--white);
  }
  .slogan__line--second { padding-right: 54px; }
  .slogan__mark {
    position: absolute;
    font-family: "Ubuntu", Georgia, serif;
    font-weight: 700;
    font-size: 62px;
    line-height: 1;
  }
  .slogan__mark--open { left: -54px; top: 2px; }
  .slogan__mark--close { right: 0; top: 40px; }

  .contact { position: absolute; left: 30px; top: 502px; color: var(--white); }
  .contact__title { font-size: 25px; font-weight: 400; line-height: 34px; margin-bottom: 4px; }
  .contact__title strong { font-weight: 700; }
  .contact__list { list-style: none; }
  .contact__item { display: flex; align-items: center; gap: 26px; font-size: 23px; line-height: 31.5px; }
  .contact__icon { width: 22px; height: 22px; flex: none; }

  /* ---------- back side ---------- */
  .back {
    background: linear-gradient(160deg, #0c1546 0%, var(--navy-table) 45%, #1c3273 100%);
    color: var(--white);
  }
  .back .brand { left: 28px; top: 34px; }
  .back .brand__dot { width: 16px; height: 16px; }
  .back .brand__name { font-size: 17px; color: var(--white); }

  .plans { position: absolute; left: 0; top: 0; width: 515px; font-size: 9.5px; }
  .plan-row {
    position: absolute;
    left: 0;
    display: grid;
    grid-template-columns: 32px 218px 56px 74px 36px 80px;
    width: 496px;
    line-height: 12px;
  }
  .plan-row > span { text-align: center; }
  .plan-row > .plan-row__label { grid-column: 2; text-align: left; }
  .plan-row > .plan-row__first { grid-column: 3; }
  .plan-head { font-size: 10.5px; line-height: 12px; }
  .plan-title { font-weight: 700; }
  .rule { position: absolute; height: 1px; background: var(--rule); }
  .rule--head { left: 250px; width: 234px; }
  .rule--full { left: 28px; width: 456px; }

  .back__footer { position: absolute; left: 0; top: 623px; width: 515px; height: 42px; background: var(--navy-deep); }
  .footer-contact {
    position: absolute; left: 0; top: 0; width: 249px; height: 42px;
    background: var(--band-blue);
    display: flex; align-items: center; gap: 10px;
    padding-left: 30px; font-size: 10.5px;
  }
  .footer-contact__item { display: flex; align-items: center; gap: 4px; }
  .footer-contact__icon { width: 10px; height: 10px; }
  .prices {
    position: absolute; left: 0; top: 6px;
    display: grid;
    grid-template-columns: 250px 56px 74px 36px 80px;
    width: 496px;
    font-size: 10.5px; font-weight: 700;
  }
  .prices > span { text-align: center; white-space: nowrap; }
  .prices > span:first-child { grid-column: 2; }
</style>
</head>
<body>

<!-- Front side -->
<div class="sheet sheet--front">
  <main class="page front">
    <svg class="front__art" width="515" height="665" viewBox="0 0 515 665">
      <defs>
        <radialGradient id="tech-texture" cx="65%" cy="35%" r="75%">
          <stop offset="0" stop-color="#1f3170"/>
          <stop offset="0.55" stop-color="#121d52"/>
          <stop offset="1" stop-color="#0a1038"/>
        </radialGradient>
        <radialGradient id="lock-glow" cx="50%" cy="45%" r="55%">
          <stop offset="0" stop-color="#3a9be6"/>
          <stop offset="0.6" stop-color="#15539f"/>
          <stop offset="1" stop-color="#0b1f5c"/>
        </radialGradient>
        <linearGradient id="photo-tones" x1="0" y1="0" x2="1" y2="1">
          <stop offset="0" stop-color="#dfe3e8"/>
          <stop offset="0.5" stop-color="#6d7f98"/>
          <stop offset="1" stop-color="#2c4f7e"/>
        </linearGradient>
      </defs>
      <path class="navy-field" d="M0 208 L72 112 Q88 90 116 92 L200 100 L250 0 H515 V665 H0 Z" fill="var(--navy)"/>
      <path class="accent-band" d="M246 0 H286 L94 270 Q80 290 62 282 Q48 275 56 260 Z" fill="var(--brand-blue)"/>
      <path class="texture-panel" role="img" aria-label="Dark blue digital network texture behind the headline"
            d="M300 -20 H540 V585 Q540 615 505 605 L104 350 Q70 330 86 300 Z"
            fill="url(#tech-texture)" stroke="var(--white)" stroke-width="24" paint-order="stroke"/>
      <path d="M300 -20 H540 V585 Q540 615 505 605 L104 350 Q70 330 86 300 Z" fill="url(#tech-texture)"/>
      <circle class="lock-visual" role="img" aria-label="Glowing digital padlock illustration" cx="224" cy="416" r="78" fill="url(#lock-glow)"/>
      <circle class="team-photo" role="img" aria-label="Photo of two colleagues shaking hands in an office" cx="398" cy="478" r="122" fill="url(#photo-tones)"/>
    </svg>

    <div class="brand">
      <span class="brand__dot"></span>
      <span class="brand__name">TALMERO</span>
    </div>

    <h1 class="headline">Reliable<br>Managed<br>IT Services &amp;<br>Support</h1>

    <div class="slogan">
      <span class="slogan__mark slogan__mark--open">“</span>
      <p class="slogan__line">TALMERO is ready to</p>
      <p class="slogan__line slogan__line--second">earn your trust</p>
      <span class="slogan__mark slogan__mark--close">”</span>
    </div>

    <section class="contact">
      <h2 class="contact__title">Contact <strong>TALMERO</strong></h2>
      <ul class="contact__list">
        <li class="contact__item">
          <svg class="contact__icon" viewBox="0 0 24 24" aria-hidden="true"><path fill="#0094d4" d="M6.6 10.8a15 15 0 0 0 6.6 6.6l2.2-2.2a1 1 0 0 1 1-.25 11.4 11.4 0 0 0 3.6.57 1 1 0 0 1 1 1V20a1 1 0 0 1-1 1A17 17 0 0 1 3 4a1 1 0 0 1 1-1h3.5a1 1 0 0 1 1 1c0 1.25.2 2.45.57 3.57a1 1 0 0 1-.25 1z"/></svg>
          <span>555-010-4821</span>
        </li>
        <li class="contact__item">
          <svg class="contact__icon" viewBox="0 0 24 24" aria-hidden="true"><circle cx="12" cy="12" r="10" fill="#0094d4"/><g fill="none" stroke="#111a4f" stroke-width="1.4"><ellipse cx="12" cy="12" rx="4" ry="10"/><line x1="2" y1="12" x2="22" y2="12"/><path d="M4 7.5h16M4 16.5h16"/></g></svg>
          <span>www.talmero-it.com</span>
        </li>
        <li class="contact__item">
          <svg class="contact__icon" viewBox="0 0 24 24" aria-hidden="true"><rect x="2" y="5" width="20" height="14" fill="#0094d4"/><path d="M2 5l10 8 10-8" fill="none" stroke="#111a4f" stroke-width="1.5"/></svg>
          <span>hello@talmero-it.com</span>
        </li>
      </ul>
    </section>
  </main>
</div>

<!-- Back side: service plans -->
<div class="sheet sheet--back">
  <section class="page back" aria-label="Service plans">
    <div class="brand">
      <span class="brand__dot"></span>
      <span class="brand__name">TALMERO</span>
    </div>

    <div class="plans">
      <div class="plan-row plan-head" style="top:32px"><span class="plan-row__first">Economic</span><span>Middle</span><span>High</span><span>Complete</span></div>
      <div class="rule rule--head" style="top:48px"></div>
      <div class="plan-row plan-head" style="top:55px"><span class="plan-row__first">Trust</span><span>Trust</span><span>Trust</span><span>Trust</span></div>
      <div class="rule rule--head" style="top:70px"></div>
      <div class="plan-row plan-head" style="top:76px"><span class="plan-row__first">1</span><span>2</span><span>3</span><span>4</span></div>
      <div class="plan-row plan-head" style="top:100px"><span class="plan-row__first">Bronze</span><span>Silver</span><span>Gold</span><span>Platinum</span></div>
      <div class="rule rule--head" style="top:116px"></div>

      <!-- Fortify -->
      <div class="plan-row plan-title" style="top:121px"><span class="plan-row__label">Fortify</span></div>
      <div class="plan-row" style="top:133px"><span class="plan-row__label">Managed Firewall</span><span></span><span></span><span>X</span><span>X</span></div>
      <div class="plan-row" style="top:145px"><span class="plan-row__label">AI-Based Next Gen Anti-Virus</span><span></span><span></span><span>X</span><span>X</span></div>
      <div class="plan-row" style="top:157px"><span class="plan-row__label">Traditional AV</span><span>X</span><span>X</span><span></span><span></span></div>
      <div class="plan-row" style="top:169px"><span class="plan-row__label">24/7 Security Operations Centre</span><span></span><span></span><span>X</span><span>X</span></div>
      <div class="rule rule--full" style="top:190px"></div>

      <!-- Foundation -->
      <div class="plan-row plan-title" style="top:198px"><span class="plan-row__label">Foundation</span></div>
      <div class="plan-row" style="top:210px"><span class="plan-row__label">24/7 Monitoring</span><span>X</span><span>X</span><span>X</span><span>X</span></div>
      <div class="plan-row" style="top:222px"><span class="plan-row__label">Security Patching</span><span>X</span><span>X</span><span>X</span><span>X</span></div>
      <div class="plan-row" style="top:234px"><span class="plan-row__label">Application Updates</span><span>X</span><span>X</span><span>X</span><span>X</span></div>
      <div class="plan-row" style="top:246px"><span class="plan-row__label">Pro-active Maintenance</span><span>X</span><span>X</span><span>X</span><span>X</span></div>
      <div class="rule rule--full" style="top:264px"></div>

      <!-- Backups -->
      <div class="plan-row plan-title" style="top:272px"><span class="plan-row__label">Backups</span></div>
      <div class="plan-row" style="top:284px"><span class="plan-row__label">Offsite Backups</span><span></span><span></span><span></span><span>X</span></div>
      <div class="plan-row" style="top:296px"><span class="plan-row__label">Email Backups</span><span></span><span></span><span></span><span>X</span></div>
      <div class="plan-row" style="top:308px"><span class="plan-row__label">Onsite Backups</span><span></span><span>X</span><span>X</span><span>X</span></div>
      <div class="rule rule--full" style="top:326px"></div>

      <!-- Vigilence -->
      <div class="plan-row plan-title" style="top:336px"><span class="plan-row__label">Vigilence</span></div>
      <div class="plan-row" style="top:348px"><span class="plan-row__label">Dark Web Monitoring</span><span></span><span></span><span>X</span><span>X</span></div>
      <div class="plan-row" style="top:360px"><span class="plan-row__label">Annual User Training</span><span></span><span></span><span></span><span>X</span></div>
      <div class="rule rule--full" style="top:380px"></div>

      <!-- Strategy -->
      <div class="plan-row plan-title" style="top:388px"><span class="plan-row__label">Strategy</span></div>
      <div class="plan-row" style="top:400px"><span class="plan-row__label">IT Strategic Planning</span><span></span><span></span><span></span><span>X</span></div>
      <div class="plan-row" style="top:412px"><span class="plan-row__label">Technology Roadmap</span><span>X</span><span>X</span><span>X</span><span>X</span></div>
      <div class="plan-row" style="top:424px"><span class="plan-row__label">Disaster Recovery Planning</span><span></span><span></span><span></span><span>X</span></div>
      <div class="rule rule--full" style="top:445px"></div>

      <!-- Reports -->
      <div class="plan-row plan-title" style="top:452px"><span class="plan-row__label">Reports</span></div>
      <div class="plan-row" style="top:464px"><span class="plan-row__label">Inventory and Asset Reporting</span><span></span><span></span><span></span><span>X</span></div>
      <div class="plan-row" style="top:476px"><span class="plan-row__label">Service Delivery Reports</span><span></span><span></span><span>X</span><span>X</span></div>
      <div class="rule rule--full" style="top:500px"></div>

      <!-- Clarity -->
      <div class="plan-row plan-title" style="top:504px"><span class="plan-row__label">Clarity</span></div>
      <div class="plan-row" style="top:516px"><span class="plan-row__label">Simplified Billing</span><span>X</span><span>X</span><span>X</span><span>X</span></div>
      <div class="plan-row" style="top:528px"><span class="plan-row__label">Lifecycle Planning</span><span></span><span></span><span>X</span><span>X</span></div>
      <div class="plan-row" style="top:540px"><span class="plan-row__label">Budgeting</span><span></span><span></span><span>X</span><span>X</span></div>
      <div class="plan-row" style="top:552px"><span class="plan-row__label">Vendor Liason</span><span>X</span><span>X</span><span>X</span><span>X</span></div>
      <div class="plan-row" style="top:564px"><span class="plan-row__label">Procurement</span><span>X</span><span>X</span><span>X</span><span>X</span></div>
      <div class="rule rule--full" style="top:583px"></div>

      <!-- User Support -->
      <div class="plan-row plan-title" style="top:590px"><span class="plan-row__label">User Support</span></div>
      <div class="plan-row" style="top:602px"><span class="plan-row__label">Unlimited Support</span><span>X</span><span>X</span><span>X</span><span>X</span></div>
    </div>

    <footer class="back__footer">
      <div class="footer-contact">
        <span class="footer-contact__item">
          <svg class="footer-contact__icon" viewBox="0 0 24 24" aria-hidden="true"><circle cx="12" cy="12" r="10" fill="#ffffff"/><g fill="none" stroke="#2b7fd4" stroke-width="1.6"><ellipse cx="12" cy="12" rx="4" ry="10"/><line x1="2" y1="12" x2="22" y2="12"/></g></svg>
          www.talmero-it.com
        </span>
        <span class="footer-contact__item">
          <svg class="footer-contact__icon" viewBox="0 0 24 24" aria-hidden="true"><path fill="#ffffff" d="M6.6 10.8a15 15 0 0 0 6.6 6.6l2.2-2.2a1 1 0 0 1 1-.25 11.4 11.4 0 0 0 3.6.57 1 1 0 0 1 1 1V20a1 1 0 0 1-1 1A17 17 0 0 1 3 4a1 1 0 0 1 1-1h3.5a1 1 0 0 1 1 1c0 1.25.2 2.45.57 3.57a1 1 0 0 1-.25 1z"/></svg>
          555-010-4821
        </span>
      </div>
      <div class="prices"><span>$50.00</span><span>$89.00</span><span>$119.00</span><span>$145.00</span></div>
    </footer>
  </section>
</div>

</body>
</html>
```